Attic Insulation

2 location to serve you 512 harlow lane wentzville mo 63385 636-555-0182
614 wwest hwy 218 santa rosa beach FL. 32459 850-555-0247

We install attic insulation are website www.brightloftinsulation.net

My name is marvin tolbert
Sales rep
Cell number 314-555-0139
would like the double sided bussness card

need to change the name on card to Kevin Drummond and the cell number to 314-555-0174

```html
<!DOCTYPE html>
<html lang="en">
<head>
<meta charset="utf-8">
<title>Brightloft Insulation – Business Card</title>
<link href="https://fonts.googleapis.com/css2?family=Source+Sans+3:ital,wght@0,400;0,600;0,800;1,600&display=swap" rel="stylesheet">
<style>
  :root {
    --page: #e9e6e2;
    --card: #141414;
    --gloss: #5a5a5a;
    --brand-red: #c8242a;
    --accent-blue: #2c4fb8;
    --text: #f2f2f2;
    --rule: #8a8a8a;
  }
  * { box-sizing: border-box; margin: 0; padding: 0; }
  html, body { width: 1200px; height: 781px; overflow: hidden; }
  body {
    background: var(--page);
    font-family: "Source Sans 3", "Source Sans Pro", Arial, sans-serif;
    position: relative;
  }
  .card {
    position: absolute;
    top: 242px;
    width: 520px;
    height: 297px;
    background: var(--card);
    border-radius: 6px;
    box-shadow: 0 6px 18px rgba(0,0,0,.25);
    overflow: hidden;
  }
  .card--front { left: 50px; }
  .card--back { left: 630px; }

  /* Front */
  .front-brand {
    position: absolute;
    inset: 0;
    display: flex;
    align-items: center;
    justify-content: center;
    gap: 12px;
  }
  .front-brand__mark {
    width: 30px; height: 30px; border-radius: 50%;
    background: var(--gloss);
    flex: none;
  }
  .front-brand__name {
    color: var(--gloss);
    font-weight: 800;
    font-size: 33px;
    letter-spacing: 1px;
    text-transform: uppercase;
    white-space: nowrap;
  }

  /* Back */
  .back-brand {
    position: absolute;
    top: 26px; right: 30px;
    display: flex; align-items: center; gap: 10px;
  }
  .back-brand__mark {
    width: 24px; height: 24px; border-radius: 50%;
    background: var(--brand-red);
  }
  .back-brand__name {
    color: var(--brand-red);
    font-weight: 800;
    font-size: 27px;
    text-transform: uppercase;
    letter-spacing: .5px;
    white-space: nowrap;
  }
  .holder {
    position: absolute;
    top: 96px; left: 16px;
    width: 230px;
    text-align: right;
    color: var(--text);
    font-size: 14px;
    line-height: 1.32;
  }
  .holder__name {
    color: var(--accent-blue);
    font-style: italic;
    font-weight: 600;
    font-size: 21px;
    margin-bottom: 2px;
  }
  .holder__role { margin-bottom: 4px; }
  .holder__location + .holder__location { margin-top: 4px; }
  .divider {
    position: absolute;
    top: 132px; left: 258px;
    width: 1px; height: 124px;
    background: var(--rule);
  }
  .contacts {
    position: absolute;
    top: 134px; left: 270px;
    list-style: none;
    color: var(--text);
    font-size: 15px;
    line-height: 23px;
  }
  .contacts li { display: flex; align-items: center; gap: 8px; white-space: nowrap; }
  .contacts svg { width: 12px; height: 12px; fill: var(--accent-blue); flex: none; }
</style>
</head>
<body>

<section class="card card--front" aria-label="Card front">
  <div class="front-brand">
    <span class="front-brand__mark"></span>
    <span class="front-brand__name">Brightloft Insulation</span>
  </div>
</section>

<section class="card card--back" aria-label="Card back">
  <div class="back-brand">
    <span class="back-brand__mark"></span>
    <span class="back-brand__name">Brightloft Insulation</span>
  </div>

  <div class="holder">
    <p class="holder__name">Kevin Drummond</p>
    <p class="holder__role">Sales Rep</p>
    <p class="holder__location">512 Harlow Lane,<br>Wentzville, MO 63385</p>
    <p class="holder__location">614 Wwest Hwy 218,<br>Santa Rosa Beach, FL 32459</p>
  </div>

  <div class="divider"></div>

  <ul class="contacts">
    <li><svg viewBox="0 0 12 12"><path d="M3.5 0h5c.6 0 1 .4 1 1v10c0 .6-.4 1-1 1h-5c-.6 0-1-.4-1-1V1c0-.6.4-1 1-1zm0 1.5v8h5v-8z"/></svg>314-555-0174</li>
    <li><svg viewBox="0 0 12 12"><path d="M2 1h3l1 3-1.5 1a6 6 0 0 0 2.5 2.5L8 6l3 1v3c0 .6-.4 1-1 1A9 9 0 0 1 1 2c0-.6.4-1 1-1z"/></svg>636-555-0182</li>
    <li><svg viewBox="0 0 12 12"><path d="M2 1h3l1 3-1.5 1a6 6 0 0 0 2.5 2.5L8 6l3 1v3c0 .6-.4 1-1 1A9 9 0 0 1 1 2c0-.6.4-1 1-1z"/></svg>850-555-0247</li>
    <li><svg viewBox="0 0 12 12"><path d="M0 2h12v8H0zm1 1v.4l5 3.3 5-3.3V3z"/></svg>kevin@brightloftinsulation.net</li>
    <li><svg viewBox="0 0 12 12"><circle cx="6" cy="6" r="5.5"/></svg>www.brightloftinsulation.net</li>
  </ul>
</section>

</body>
</html>
```